Flyer Design for Promoting Arborist Business

Hi guys,
***UPDATE: File pack is available here: https://www.filecrate-share.net/sh/q7x2kd91mvz4ab/BXR5tnwPqLeZsHuYdJ0c_b?dl=0
We've are a high-end arborist business in Edinburgh and we're now looking to create some promotional flyers to attract new business.
This is an open brief and we're looking for inspiration from our designer.
Our target market for the flyers is people who cannot readily access our online material (e.g. elderly people without internet access), so therefore has to be easily understood.
Trust is a central part of our business and we'd like our photographs on the flyer to build that trust.
The primary method of contact will be telephone, therefore we'd like our phone numbers to be front and centre.
You can see our website here: www.moravelmtreecare.com
We have a full pack of design material for our logo which can be shared. This includes colours, fonts and logo. It's all as per our website.
Inspire us!
Best,
Lewis

```html
<!DOCTYPE html>
<html lang="en">
<head>
<meta charset="utf-8">
<title>Moravelm Tree Care Flyer</title>
<link href="https://fonts.googleapis.com/css2?family=Cinzel:wght@500&family=Tinos&family=Archivo:wght@800&family=PT+Sans:wght@400;700&family=Roboto:wght@500;700&display=swap" rel="stylesheet">
<style>
:root{
  --red:#b3151c;
  --red-dark:#8a0e13;
  --red-text:#b5121b;
  --ink:#1a1a1a;
  --grey-text:#6b6b6b;
  --white:#ffffff;
  --photo-dark:#2b2420;
  --photo-mid:#5a4a3c;
  --photo-light:#8a7a62;
}
*{margin:0;padding:0;box-sizing:border-box}
html,body{width:912px;height:1200px;overflow:hidden;background:#f2f2f2}
.flyer{position:absolute;left:0;top:0;width:875px;height:1240px;background:var(--white);transform:scale(1.04229,0.96774);transform-origin:0 0;overflow:hidden;font-family:"PT Sans",sans-serif}
.hero-photo{position:absolute;left:0;top:0;width:875px;height:480px;background:linear-gradient(120deg,var(--photo-dark) 0%,#3a302a 35%,var(--photo-mid) 65%,var(--photo-light) 100%)}
.hero-shade{position:absolute;left:0;top:0;width:875px;height:480px;background:linear-gradient(90deg,rgba(0,0,0,.55) 0%,rgba(0,0,0,.2) 55%,rgba(0,0,0,0) 100%)}
.header-shapes{position:absolute;left:0;top:0}
.emergency{position:absolute;right:22px;top:30px;font-family:"Tinos",serif;font-size:25px;color:var(--white);letter-spacing:.5px}
.brand{position:absolute;left:28px;top:96px;font-family:"Cinzel",serif;font-weight:500;color:var(--ink)}
.brand-name{display:block;font-size:46px;line-height:52px;letter-spacing:1px}
.brand-sub{display:block;font-size:28px;line-height:34px;letter-spacing:12px}
.headline{position:absolute;left:28px;top:283px;font-family:"Archivo",sans-serif;font-weight:800;font-size:31px;line-height:38px;color:var(--white);letter-spacing:1px}
.photo-circle{position:absolute;border-radius:50%;border:4px solid var(--white);box-shadow:0 3px 8px rgba(0,0,0,.4)}
.photo-circle.small{left:528px;top:391px;width:132px;height:132px;background:radial-gradient(circle at 40% 40%,#b9c2c8,#6b7a62 70%,#4d5a40)}
.photo-circle.large{left:675px;top:350px;width:182px;height:182px;background:linear-gradient(180deg,#a9b7c2 0%,#8a9a6a 55%,#c9b98a 100%)}
.services{position:absolute;left:502px;top:480px;width:356px;height:595px;background:linear-gradient(160deg,var(--red) 0%,#a01218 60%,var(--red-dark) 100%);border-radius:0 0 22px 22px;box-shadow:0 4px 10px rgba(0,0,0,.25)}
.services-tab{position:absolute;left:502px;top:550px;width:243px;height:42px;background:linear-gradient(90deg,#111 0%,#333 85%,#222 100%);border-radius:0 14px 14px 0;color:var(--white);font-family:"Roboto",sans-serif;font-weight:500;font-size:19px;line-height:42px;padding-left:52px}
.service-list{position:absolute;left:518px;top:605px;list-style:none}
.service-list li{display:flex;align-items:center;height:31.3px;color:var(--white);font-size:22px}
.service-list svg{width:18px;height:18px;margin-right:12px;flex:none}
.intro-title{position:absolute;left:27px;top:528px;width:436px;font-size:25.5px;line-height:33px;color:var(--red-text);font-weight:700;letter-spacing:-.2px}
.intro-title span{font-weight:400}
.intro-text{position:absolute;left:27px;width:434px;font-size:21px;line-height:28.7px;color:var(--grey-text);text-align:justify}
.intro-text.first{top:612px}
.intro-text.second{top:838px;text-align:left}
.badge{position:absolute}
.badge.one{left:27px;top:988px;width:124px;height:94px;border:3px solid var(--red);border-radius:8px;background:linear-gradient(180deg,#fff 0%,#fff 72%,var(--red) 72%)}
.badge.two{left:180px;top:990px;width:70px;height:90px;border-radius:6px;background:#e4e4e4}
.footer{position:absolute;left:0;top:1090px}
.phone-pill{position:absolute;left:215px;top:1124px;width:445px;height:58px;border-radius:29px;background:linear-gradient(180deg,#d21f26 0%,var(--red) 55%,var(--red-dark) 100%);box-shadow:0 3px 6px rgba(0,0,0,.5);display:flex;align-items:center;justify-content:center;gap:14px;color:var(--white);font-family:"Roboto",sans-serif;font-weight:700;font-size:40px;letter-spacing:2px}
.phone-pill svg{width:38px;height:38px}
.website{position:absolute;left:0;width:875px;top:1196px;text-align:center;color:var(--white);font-size:25px;letter-spacing:1.5px}
</style>
</head>
<body>
<div class="flyer">
  <div class="hero-photo" role="img" aria-label="Tree surgeon in a helmet cutting a large trunk with a chainsaw above a tiled roof"></div>
  <div class="hero-shade"></div>
  <svg class="header-shapes" width="875" height="480" viewBox="0 0 875 480">
    <path d="M0 0H875V105H520C470 105 445 128 415 168C390 200 372 210 340 210H0Z" fill="#ffffff"/>
    <path d="M428 0H875V80H505C482 80 470 70 455 42Z" fill="#b3151c"/>
  </svg>
  <div class="emergency">24/7 EMERGENCY SERVICE</div>
  <div class="brand"><span class="brand-name">MORAVELM</span><span class="brand-sub">TREE CARE</span></div>
  <h1 class="headline">PROFESSIONAL<br>EDINBURGH-BASED<br>TREE SURGEONS</h1>

  <div class="services"></div>
  <div class="photo-circle small" role="img" aria-label="Arborist working among bare branches"></div>
  <div class="photo-circle large" role="img" aria-label="Two arborists in hi-vis vests standing beneath a large tree"></div>
  <div class="services-tab">OUR SERVICES</div>
  <svg width="0" height="0" style="position:absolute">
    <symbol id="chev" viewBox="0 0 18 18"><circle cx="9" cy="9" r="7.5" fill="none" stroke="#fff" stroke-width="1.5"/><path d="M7.5 5.5L11 9L7.5 12.5" fill="none" stroke="#fff" stroke-width="1.8"/></symbol>
  </svg>
  <ul class="service-list">
    <li><svg><use href="#chev"/></svg>Aerial Pruning</li>
    <li><svg><use href="#chev"/></svg>Aerial Dismantling</li>
    <li><svg><use href="#chev"/></svg>Clear Felling</li>
    <li><svg><use href="#chev"/></svg>Crown Lifts</li>
    <li><svg><use href="#chev"/></svg>Crown Reductions</li>
    <li><svg><use href="#chev"/></svg>Emergency Response</li>
    <li><svg><use href="#chev"/></svg>Garden Clearance</li>
    <li><svg><use href="#chev"/></svg>Sectional Felling</li>
    <li><svg><use href="#chev"/></svg>Site Clearance</li>
    <li><svg><use href="#chev"/></svg>Storm Damage</li>
    <li><svg><use href="#chev"/></svg>Stump Removal</li>
    <li><svg><use href="#chev"/></svg>Tree Surveys</li>
    <li><svg><use href="#chev"/></svg>Waste Removal</li>
    <li><svg><use href="#chev"/></svg>Wood Chipping</li>
  </ul>

  <h2 class="intro-title">Looking for a professional tree surgeon in Edinburgh? <span>Give us a try!</span></h2>
  <p class="intro-text first">We're friendly, professional and dependable with a discerning eye for detail and a passion for tree care. Whether you need one or more trees reduced, trimmed or removed, we offer bespoke tree services to residential customers as well as commercial enterprises and government organisations.</p>
  <p class="intro-text second">We offer a free planning application service to manage the necessary permissions<br>for trees with Tree Protection Orders (TPOs) and in Conservation Areas.</p>
  <div class="badge one"></div>
  <div class="badge two"></div>

  <svg class="footer" width="875" height="150" viewBox="0 0 875 150">
    <defs><linearGradient id="footBlack" x1="0" y1="0" x2="0" y2="1"><stop offset="0" stop-color="#2a2a2a"/><stop offset="1" stop-color="#0d0d0d"/></linearGradient></defs>
    <path d="M0 10C180 30 320 48 440 48C560 48 700 30 875 5V150H0Z" fill="#8a0e13"/>
    <path d="M0 28C180 45 320 60 440 60C560 60 700 42 875 20V150H0Z" fill="#ffffff"/>
    <path d="M0 34C180 50 320 66 440 66C560 66 700 48 875 26V150H0Z" fill="url(#footBlack)"/>
  </svg>
  <div class="phone-pill">
    <svg viewBox="0 0 38 38"><circle cx="19" cy="19" r="16" fill="none" stroke="#fff" stroke-width="3"/><path d="M13 11c1-1 2-1 3 0l2 3c.5 1 0 2-1 2.5l-1 .8c1 2.5 3 4.5 5.5 5.5l.8-1c.5-1 1.5-1.5 2.5-1l3 2c1 1 1 2 0 3l-1.5 1.5c-5 1-13-7-14.5-13z" fill="#fff"/></svg>
    0131 496 0182
  </div>
  <div class="website">www.moravelmtreecare.com</div>
</div>
</body>
</html>
```